Company Brochure / Data Sheet Template Design

We need a brochure / data sheet template for a new company based in Texas focused on Information Technology consulting. The design should instill professionalism, confidence, and strength. The company name is Ferrow Systems Collective, so you can incorporate alchemy concept into the design. I have attached the logo for the company. Our customers are medium and large businesses. We would like the top bar to incorporate black background to complement the black logo. Alternatively, you can incorporate the blue color and the white logo.

We will use this template for all corporate market materials. It should be usable for 1-6 pages documents.

Below are a couple examples by large technology companies:
http://www.quintrel.com/files/pdf/products/nodespan/Quintrel-NodeSpan-nsOM-Pricing-FAQs.pdf
https://www.pellova.com/content/dam/pellova/en_us/documents/products-solutions/the-pellova-advantage-for-deskform-10.pdf

Please let us know if you have any questions.

Target Market(s)

Large Corporations and Small-to-Medium sized businesses

Industry/Entity Type

Information Technology

Font styles to use
Other font styles liked:
• Copperplate Gothic or something similar to the logo design

Requirements
Must have
• Design on the top of the page cover cross the entire page. Incorporate www.ferrowsyscollective.com or logo at the bottom of the page. Incorporate page numbers at the bottom of the page. Template should have the ability to incorporate 1 or 2 columns of content.
• This should match the look and feel of the logo.
Nice to have
• Template should have the ability to incorporate 1 or 2 columns of content
• Incorporate font and blue color into the design.
• Blue color could be incorporated into the headings of the content
Should not have
• This needs to be professional, not playful.

```html
<!DOCTYPE html>
<html lang="en">
<head>
<meta charset="utf-8">
<title>Ferrow Systems Collective – Data Sheet Template</title>
<link rel="stylesheet" href="https://fonts.googleapis.com/css2?family=Lato:wght@300;400&display=swap">
<style>
  :root {
    --teal: #1f9fb0;
    --teal-soft: rgba(31, 159, 176, 0.35);
    --ink: #2b3440;
    --body-ink: #5d6670;
    --rule: #b9c0c6;
    --page-top: #ffffff;
    --page-bottom: #dde2e7;
    --stage: #cfd0d2;
  }
  * { box-sizing: border-box; margin: 0; padding: 0; }
  html, body {
    width: 1200px; height: 1198px; overflow: hidden;
    background: radial-gradient(ellipse at center, #e0e1e3 0%, var(--stage) 100%);
    font-family: "Lato", Arial, sans-serif;
  }
  .page {
    position: absolute; width: 422px; height: 547px; overflow: hidden;
    background: linear-gradient(180deg, var(--page-top) 0%, var(--page-bottom) 100%);
    box-shadow: 0 2px 6px rgba(0,0,0,0.28);
  }
  .page::before {
    content: ""; position: absolute; left: 0; top: 0; width: 100%; height: 12px;
    background: var(--teal); z-index: 3;
  }
  .page--cover { left: 160px; top: 35px; }
  .page--two-col { left: 616px; top: 34px; }
  .page--one-col { left: 161px; top: 607px; }
  .page--gallery { left: 616px; top: 607px; }

  .cover-photo {
    position: absolute; inset: 0;
    background:
      linear-gradient(180deg, rgba(40,120,130,0.25), rgba(60,110,120,0.15)),
      radial-gradient(ellipse at 25% 55%, #cdb9a4 0%, #a78a6e 45%, #7b6250 100%);
  }
  .cover-copy { position: absolute; left: 210px; top: 45px; width: 200px; color: #fff; z-index: 2; }
  .cover-copy .headline { color: #fff; font-size: 24px; line-height: 24px; font-weight: 300; }
  .cover-copy .lede { color: #fff; font-size: 9px; line-height: 9.6px; margin-top: 9px; }

  .column { position: absolute; }
  .headline { font-weight: 300; color: var(--ink); font-size: 21px; line-height: 21px; letter-spacing: -0.1px; }
  .body-copy p { font-size: 8px; line-height: 8.3px; color: var(--body-ink); margin-bottom: 8px; }
  .headline + .body-copy { margin-top: 14px; }

  .accent-field {
    position: absolute; right: 0; bottom: 0; width: 190px; height: 330px; z-index: 0;
    background: radial-gradient(ellipse at 100% 80%, var(--teal-soft) 0%, rgba(31,159,176,0.12) 50%, rgba(31,159,176,0) 75%);
  }
  .column, .footer { z-index: 1; }

  .footer { position: absolute; left: 28px; right: 28px; bottom: 0; height: 120px; }
  .footer__rule { position: absolute; left: 0; right: 0; top: 0; border-top: 1px solid var(--rule); }
  .brand {
    position: absolute; left: 0; right: 0; top: 50px;
    display: flex; justify-content: center; align-items: center; gap: 6px;
    font-size: 12px; font-weight: 400; color: var(--ink); letter-spacing: 0.4px;
  }
  .brand__mark { width: 9px; height: 9px; background: var(--teal); }
  .url { position: absolute; left: 0; right: 0; top: 77px; text-align: center; font-size: 9px; color: #9aa3ab; }
  .page-number { position: absolute; right: 22px; top: 74px; font-size: 8px; color: #8a939b; }

  .page--cover .footer { left: 0; right: 0; }
  .page--cover .brand { color: #fff; }
  .page--cover .url { color: rgba(255,255,255,0.8); }

  .thumb { position: absolute; top: 51px; width: 171px; height: 76px; }
  .thumb--meeting { left: 28px; background: linear-gradient(135deg, #7a6558 0%, #c9b7a6 50%, #e9e6e2 100%); }
  .thumb--desk { left: 223px; background: linear-gradient(160deg, #1d1a17 0%, #5a3c20 45%, #b07a3c 80%, #e6e2dc 100%); }
</style>
</head>
<body>

<section class="page page--cover">
  <div class="cover-photo" role="img" aria-label="Photograph of a hand holding a smartphone showing a news site, in front of a laptop on a wooden desk"></div>
  <div class="cover-copy">
    <h1 class="headline">Veltrano enters Asia-Pacific market, dedicates itself to make strategic investments</h1>
    <p class="lede">Software provider, Veltrano, has expanded its operations to the Asia-Pacific region with the appointment of a new regional head, Dana Morrow.</p>
  </div>
  <footer class="footer">
    <div class="brand"><span class="brand__mark"></span>Ferrow Systems Collective</div>
    <div class="url">www.ferrowsyscollective.com</div>
  </footer>
</section>

<section class="page page--two-col">
  <div class="accent-field" role="img" aria-label="Soft teal tonal accent"></div>
  <article class="column" style="left:28px; top:37px; width:172px;">
    <h2 class="headline">Veltrano enters Asia-Pacific market, dedicates itself to make strategic investments</h2>
    <div class="body-copy">
      <p>Software provider, Veltrano, has expanded its operations to the Asia-Pacific region with the appointment of a new regional head, Dana Morrow.</p>
      <p>Morrow will be based at the company’s new Asia-Pacific regional office in Melbourne and will be responsible for driving revenue and overseeing sales and channel development teams in the region.</p>
      <p>Morrow said APAC continues to be one of the world’s fastest growing markets and one that actively pursues technology innovation as a means by which to create and maintain a competitive edge.</p>
      <p>“For APAC-based organisations seeking the ideal solution for managing and protecting their Corvane DocHub, WorkSuite 365, CloudLocker for Business, Mailport and other on-premises and cloud-based content, they will have direct access to the unparalleled solutions offered from Veltrano,” he added.</p>
      <p>The company said that following Corvane’s recent release of DocHub 2016, it is seeing expanded interest in its complete suite of solutions.</p>
    </div>
  </article>
  <article class="column" style="left:229px; top:37px; width:172px;">
    <h2 class="headline">Veltrano enters Asia-Pacific market, dedicates itself to make strategic investments</h2>
    <div class="body-copy">
      <p>Software provider, Veltrano, has expanded its operations to the Asia-Pacific region with the appointment of a new regional head, Dana Morrow.</p>
      <p>Morrow will be based at the company’s new Asia-Pacific regional office in Melbourne and will be responsible for driving revenue and overseeing sales and channel development teams in the region.</p>
      <p>Morrow said APAC continues to be one of the world’s fastest growing markets and one that actively pursues technology innovation as a means by which to create and maintain a competitive edge.</p>
      <p>“For APAC-based organisations seeking the ideal solution for managing and protecting their Corvane DocHub, WorkSuite 365, CloudLocker for Business, Mailport and other on-premises and cloud-based content, they will have direct access to the unparalleled solutions offered from Veltrano,” he added.</p>
      <p>The company said that following Corvane’s recent release of DocHub 2016, it is seeing expanded interest in its complete suite of solutions.</p>
    </div>
  </article>
  <footer class="footer">
    <div class="footer__rule"></div>
    <div class="brand"><span class="brand__mark"></span>Ferrow Systems Collective</div>
    <div class="url">www.ferrowsyscollective.com</div>
    <div class="page-number">1</div>
  </footer>
</section>

<section class="page page--one-col">
  <div class="accent-field" role="img" aria-label="Soft teal tonal accent"></div>
  <article class="column" style="left:28px; top:37px; width:370px;">
    <h2 class="headline">Veltrano enters Asia-Pacific market, dedicates itself to make strategic investments</h2>
    <div class="body-copy">
      <p>Software provider, Veltrano, has expanded its operations to the Asia-Pacific region with the appointment of a new regional head, Dana Morrow.</p>
      <p>Morrow will be based at the company’s new Asia-Pacific regional office in Melbourne and will be responsible for driving revenue and overseeing sales and channel development teams in the region.</p>
      <p>Morrow said APAC continues to be one of the world’s fastest growing markets and one that actively pursues technology innovation as a means by which to create and maintain a competitive edge.</p>
      <p>“For APAC-based organisations seeking the ideal solution for managing and protecting their Corvane DocHub, WorkSuite 365, CloudLocker for Business, Mailport and other on-premises and cloud-based content, they will have direct access to the unparalleled solutions offered from Veltrano,” he added.</p>
      <p>The company said that following Corvane’s recent release of DocHub 2016, it is seeing expanded interest in its complete suite of solutions.</p>
      <p>Veltrano vice-president channel and alliances, Ravi Solen, said the company was dedicated to making the necessary investments in staying close to customers and partners.</p>
    </div>
  </article>
  <article class="column" style="left:28px; top:284px; width:370px;">
    <h2 class="headline">Veltrano enters Asia-Pacific market, dedicates itself to make strategic investments</h2>
    <div class="body-copy">
      <p>Software provider, Veltrano, has expanded its operations to the Asia-Pacific region with the appointment of a new regional head, Dana Morrow.</p>
      <p>The company said that following Corvane’s recent release of DocHub 2016, it is seeing expanded interest in its complete suite of solutions.</p>
    </div>
  </article>
  <footer class="footer">
    <div class="footer__rule"></div>
    <div class="brand"><span class="brand__mark"></span>Ferrow Systems Collective</div>
    <div class="url">www.ferrowsyscollective.com</div>
    <div class="page-number">2</div>
  </footer>
</section>

<section class="page page--gallery">
  <div class="accent-field" role="img" aria-label="Soft teal tonal accent"></div>
  <div class="thumb thumb--meeting" role="img" aria-label="Photograph of a team meeting around a table with laptops"></div>
  <div class="thumb thumb--desk" role="img" aria-label="Photograph of a laptop and mouse on a dark desk in warm light"></div>
  <article class="column" style="left:28px; top:145px; width:172px;">
    <h2 class="headline">Veltrano enters Asia-Pacific market, dedicates itself to make strategic investments</h2>
    <div class="body-copy">
      <p>Software provider, Veltrano, has expanded its operations to the Asia-Pacific region with the appointment of a new regional head, Dana Morrow.</p>
      <p>Morrow will be based at the company’s new Asia-Pacific regional office in Melbourne and will be responsible for driving revenue and overseeing sales and channel development teams in the region.</p>
      <p>Morrow said APAC continues to be one of the world’s fastest growing markets and one that actively pursues technology innovation as a means by which to create and maintain a competitive edge.</p>
    </div>
  </article>
  <article class="column" style="left:223px; top:145px; width:172px;">
    <h2 class="headline">Veltrano enters Asia-Pacific market, dedicates itself to make strategic investments</h2>
    <div class="body-copy">
      <p>Software provider, Veltrano, has expanded its operations to the Asia-Pacific region with the appointment of a new regional head, Dana Morrow.</p>
      <p>Morrow will be based at the company’s new Asia-Pacific regional office in Melbourne and will be responsible for driving revenue and overseeing sales and channel development teams in the region.</p>
      <p>Morrow said APAC continues to be one of the world’s fastest growing markets and one that actively pursues technology innovation as a means by which to create and maintain a competitive edge.</p>
    </div>
  </article>
  <footer class="footer">
    <div class="footer__rule"></div>
    <div class="brand"><span class="brand__mark"></span>Ferrow Systems Collective</div>
    <div class="url">www.ferrowsyscollective.com</div>
    <div class="page-number">1</div>
  </footer>
</section>

</body>
</html>
```